Hair & Skin Product Line

I need someone to design clear product labels that can go on pink bottles. I'm looking for someone who can add graphics such as avocado and honey to the label as these are ingredients in our products. The colors we want incorporated are gold, blue, white and purple. I will upload information about our company identity and information on one label. Whoever we choose, we will use them to create 11 more labels.

Target Market(s)

Woman 25-50, Natural, straight or curly hair.

Industry/Entity Type

Beauty

```html
<!DOCTYPE html>
<html lang="en">
<head>
<meta charset="utf-8">
<title>Purely Glow Tone – Avocado &amp; Honey Shampoo Labels</title>
<link href="https://fonts.googleapis.com/css2?family=Open+Sans:wght@400;600;700&family=Righteous&display=swap" rel="stylesheet">
<style>
  :root{
    --backdrop:#4a4a4a;
    --pink-light:#f7c3cf;
    --pink:#eeadbd;
    --pink-deep:#e49fb0;
    --white:#fff8fa;
    --gold:#c9a050;
    --gold-light:#ecd9a6;
    --ink:#1c1c1c;
    --avocado-green:#8a9a3e;
    --avocado-flesh:#d6d46e;
    --honey:#e0a030;
  }
  *{box-sizing:border-box;margin:0;padding:0}
  html,body{width:1154px;height:1200px;overflow:hidden;background:var(--backdrop)}
  body{position:relative;font-family:"Open Sans",Arial,sans-serif;color:var(--white)}

  .label{
    position:absolute;top:235px;width:275px;height:730px;border-radius:14px;
    background:linear-gradient(90deg,var(--pink-deep) 0%,var(--pink-light) 35%,var(--pink) 65%,var(--pink-deep) 100%);
  }
  .label--front{left:250px}
  .label--back{left:655px}
  .label > *{position:absolute;left:0;right:0;text-align:center}

  .brand{top:86px;display:flex;justify-content:center;align-items:center;gap:6px;font-size:19px;font-weight:600;letter-spacing:.3px}
  .brand__dot{width:9px;height:9px;border-radius:50%;background:var(--gold)}

  .product-name{top:196px;font-family:"Righteous",Arial,sans-serif;font-size:47px;line-height:52px;letter-spacing:2px;text-shadow:2px 2px 0 rgba(200,120,140,.55)}

  .band{font-weight:700;text-align:center;color:var(--white)}
  .band--benefit{top:311px;left:39px!important;right:auto!important;width:196px;height:33px;line-height:33px;font-size:16.5px;
    background:linear-gradient(90deg,#a7844a,var(--gold-light) 50%,#a7844a)}
  .band--type{top:344px;left:68px!important;right:auto!important;width:139px;height:27px;line-height:27px;font-size:17px;background:var(--ink)}

  .tagline{top:384px;font-size:12.6px;line-height:15.5px}
  .rule{left:50%!important;right:auto!important;width:50px;height:2px;margin-left:-25px;background:var(--gold)}

  .hero-art{top:478px;left:9px!important;right:auto!important;width:256px;height:186px;border-radius:18px;
    background:linear-gradient(180deg,var(--avocado-green) 0%,var(--avocado-flesh) 55%,var(--honey) 100%);opacity:.85}

  .volume{top:700px;font-family:"Righteous",Arial,sans-serif;font-size:13px;letter-spacing:1.3px}

  .intro{top:106px;font-size:12.8px;line-height:15.3px;padding:0 20px}
  .heading{font-size:12.5px;font-weight:700;letter-spacing:.3px}
  .copy{left:25px!important;right:25px!important;font-size:9.4px;line-height:12.4px;text-align:justify!important;letter-spacing:.4px}
  .signoff{top:311px;font-size:12.4px;line-height:15px;font-weight:700}
  .caution{top:539px;left:25px!important;right:25px!important;font-size:9.4px;line-height:12.5px;text-align:left!important;letter-spacing:.3px}
  .distributor{top:600px;left:28px!important;text-align:left!important;font-size:9.8px;line-height:12.4px}
  .origin{top:668px;font-size:9.6px;font-weight:600;letter-spacing:.3px}
</style>
</head>
<body>

<section class="label label--front" aria-label="Front label">
  <div class="brand"><span>Purely Glow Tone</span><span class="brand__dot"></span></div>
  <h1 class="product-name">AVOCADO<br>&amp;HONEY</h1>
  <div class="band band--benefit">MOISTURE REPAIR</div>
  <div class="band band--type">SHAMPOO</div>
  <p class="tagline">Infused w/Biotin + Rosemary<br>Gently cleanses and hydrates for<br>retention, moisture and softness</p>
  <div class="rule" style="top:441px"></div>
  <div class="hero-art" role="img" aria-label="Photo of a halved avocado resting in a pool of golden honey"></div>
  <div class="volume">300 ML /10 FL OZ</div>
</section>

<section class="label label--back" aria-label="Back label">
  <p class="intro">This healthy paraben free shampoo removes buildup without feeling stripped of hair's natural oil.</p>
  <div class="rule" style="top:158px"></div>
  <h2 class="heading" style="top:173px">HOW TO ENJOY:</h2>
  <p class="copy" style="top:191px">Use in the shower on wet hair. Apply throughout the length of hair. For thicker textures, section first before applying to ensure every strand is penetrated. Using fingers or palms massage to emulsify with water until hair is clean. Follow with your favorite Purely Glow Tone Conditioning treatment.</p>
  <div class="rule" style="top:300px"></div>
  <p class="signoff">Developed by a mother and<br>daughter who love all of hue!<br>XOXO<br>Marisa &amp; Jolie</p>
  <div class="rule" style="top:380px"></div>
  <h2 class="heading" style="top:393px">HOW TO ENJOY:</h2>
  <p class="copy" style="top:414px">Organic Aloe Vera Juice, Cocamidopropyl Betaine, Decyl Glucoside, Sodium Lauryl Lactylate, Kosher Vegetable Glycerin, Castor Oil, Olive Oil, dl-Panthenol, Polyquart 10, Ethylhexylglycerin, Phenoxy&shy;ethanol(Eco-certified, gentle, paraben free preservative), Biotin, Honey, Avocado Oil, Rosemary Essential Oil, Peppermint Essential Oil, Fragrance.</p>
  <div class="rule" style="top:532px"></div>
  <p class="caution">CAUTION: For external use only. Avoid eye contact. Keep out of reach of children</p>
  <p class="distributor">Distr. By<br>Purely Glow Tone<br>Millbrook, VT<br>PurelyGlowTone.com</p>
  <p class="origin">MADE IN THE USA</p>
</section>

</body>
</html>
```